Creation of foldable A4 Leaflet to summarise my website

I need to summarize the content of my website into a 4 facecs-2 pages A4 foldable leaflet. I need the leaflet to go through the main topics of my website, with accurate descriptions and some pics taken from the website. Focusing about professionality and over 25 year experience on the field. Give also apace to our valued partners and customers
My website plmorvex.au

Target Market(s)

Industrial filtration, dust collector business

Industry/Entity Type

Industrial filtration, dust collectors market, mining, powerplant, cement industry

Font styles to use
Sans Serif

Colors
0054AA
0677BA
7BADD7
CADEEF
E8F1F8

Requirements
Must have
• clear references to my website
Nice to have
• clear and clean layout
Should not have
• dark colours other than blue and navy, as per my logo

```html
<!DOCTYPE html>
<html lang="en">
<head>
<meta charset="utf-8">
<title>Plmorvex Environmental Services – Trifold Leaflet</title>
<link href="https://fonts.googleapis.com/css2?family=Saira+Condensed:wght@700;800&family=Lexend:wght@300;400;500;600&display=swap" rel="stylesheet">
<style>
  :root {
    --stage: #c9c7c8;
    --navy: #0c2a4e;
    --navy-deep: #0a2444;
    --blue: #2e6db8;
    --sky: #47a2d6;
    --sky-light: #62b6ea;
    --mid: #3a80c8;
    --white: #ffffff;
    --ink: #111a26;
    --pale: #e8f1f8;
  }
  * { box-sizing: border-box; margin: 0; padding: 0; }
  html, body { width: 911px; height: 1200px; overflow: hidden; }
  body { background: var(--stage); position: relative; font-family: "Lexend", sans-serif; color: var(--ink); }

  .sheet { position: absolute; left: 113px; width: 674px; height: 450px; overflow: hidden; background: var(--white); }
  .sheet--outside { top: 130px; }
  .sheet--inside { top: 597px; }

  .panel { position: absolute; top: 0; height: 450px; }
  .panel--about { left: 0; width: 225px; background: var(--white); }
  .panel--contact { left: 225px; width: 224px; background: var(--navy); }
  .panel--cover { left: 449px; width: 225px; background: var(--white); }
  .panel--services { left: 0; width: 224px; background: var(--navy); }
  .panel--supply { left: 224px; width: 226px; background: var(--sky); }
  .panel--network { left: 450px; width: 224px; background: var(--white); }

  .display { font-family: "Saira Condensed", sans-serif; font-weight: 800; text-transform: uppercase; letter-spacing: 0.3px; line-height: 1; }
  .section-title { position: absolute; left: 0; right: 0; text-align: center; font-size: 21px; }
  .section-title .accent { color: var(--blue); }
  .divider { position: absolute; height: 2px; width: 45px; left: 50%; margin-left: -22.5px; background: var(--sky-light); }
  .divider::after { content: ""; position: absolute; left: 50%; top: -1.5px; width: 5px; height: 5px; margin-left: -2.5px; border-radius: 50%; background: var(--sky-light); }

  /* About */
  .about-title { position: absolute; left: 19px; top: 20px; font-size: 22px; color: var(--navy); }
  .about-title .accent { color: var(--blue); }
  .about-divider { position: absolute; left: 19px; top: 48px; width: 48px; height: 2px; background: var(--blue); }
  .about-divider::after { content: ""; position: absolute; right: -2px; top: -1.5px; width: 5px; height: 5px; border-radius: 50%; background: var(--blue); }
  .about-subtitle { position: absolute; left: 18px; top: 58px; width: 190px; font-size: 12px; font-weight: 500; line-height: 15px; color: var(--ink); }
  .about-body { position: absolute; left: 18px; top: 92px; width: 187px; font-size: 7.9px; line-height: 14.1px; text-align: justify; font-weight: 300; color: var(--ink); }
  .about-photo { position: absolute; left: 0; top: 244px; width: 225px; height: 206px; clip-path: polygon(0 0, 100% 47.5%, 100% 100%, 0 100%); background: linear-gradient(160deg, #c8cdd2, #7e858b 45%, #3d4248); }
  .badge { position: absolute; left: 141px; top: 234px; width: 72px; height: 72px; background: var(--navy); clip-path: polygon(29% 0,71% 0,100% 29%,100% 71%,71% 100%,29% 100%,0 71%,0 29%); color: var(--white); text-align: center; padding-top: 23px; }
  .badge-years { font-size: 14px; display: block; }
  .badge-label { font-size: 9px; display: block; margin-top: 1px; }

  /* Contact */
  .contact-title { top: 41px; color: var(--white); }
  .contact-divider { top: 68px; }
  .contact-icon { position: absolute; left: 50%; width: 22px; height: 22px; margin-left: -11px; border-radius: 50%; background: var(--sky-light); display: flex; align-items: center; justify-content: center; }
  .contact-icon svg { width: 12px; height: 12px; }
  .contact-phone { position: absolute; left: 0; right: 0; top: 122px; text-align: center; font-size: 28px; color: var(--white); font-weight: 700; }
  .contact-email { position: absolute; left: 0; right: 0; top: 191px; text-align: center; font-size: 12px; color: var(--white); font-weight: 300; }
  .contact-social { position: absolute; left: 50%; top: 218px; width: 22px; height: 22px; margin-left: -11px; border-radius: 50%; background: var(--sky-light); }
  .contact-social-name { position: absolute; left: 0; right: 0; top: 243px; text-align: center; font-size: 7px; color: var(--white); font-weight: 300; }
  .contact-photo { position: absolute; left: 9px; top: 263px; width: 215px; height: 187px; clip-path: polygon(0 42.3%, 100% 0, 100% 100%, 0 100%); background: linear-gradient(115deg, #5f656b, #dfe2e4 40%, #8c9298 70%, #eef0f1); }
  .contact-strip { position: absolute; left: 0; top: 342px; width: 9px; height: 108px; background: linear-gradient(var(--sky-light), var(--mid)); }
  .contact-bars { position: absolute; left: 213px; top: 163px; width: 11px; height: 103px; background: linear-gradient(var(--sky-light) 0 30%, #4a92d6 30% 55%, #3a7ccc 55% 80%, #2b62b4 80%); }

  /* Cover */
  .cover-photo { position: absolute; left: 0; top: 0; width: 225px; height: 342px; background: linear-gradient(170deg, #c7ced6, #8f9cab 40%, #2f4f7e 65%, #d9c78f 88%, #f4efe2); }
  .brand-box { position: absolute; left: 87px; top: 0; width: 138px; height: 84px; background: var(--white); }
  .brand { position: absolute; left: 92px; top: 20px; display: flex; align-items: center; gap: 5px; }
  .brand-dot { width: 22px; height: 22px; border-radius: 50%; background: var(--blue); flex: none; }
  .brand-name { font-size: 14px; font-weight: 600; color: var(--navy); letter-spacing: 0.6px; line-height: 1; }
  .brand-tag { position: absolute; left: 119px; top: 40px; font-size: 6.3px; font-weight: 600; letter-spacing: 1.3px; color: var(--blue); line-height: 9px; text-align: center; }
  .cover-corner { position: absolute; left: 87px; top: 84px; width: 138px; height: 51px; background: var(--navy); clip-path: polygon(0 0, 100% 52%, 100% 100%); }
  .cover-panel { position: absolute; left: 0; top: 263px; width: 199px; height: 187px; background: var(--navy); clip-path: polygon(0 0, 100% 42.3%, 100% 100%, 0 100%); }
  .cover-bars { position: absolute; left: 199px; top: 342px; width: 26px; height: 108px; background: linear-gradient(var(--sky-light) 0 28%, #4a92d6 28% 55%, #3a7ccc 55% 80%, #2b62b4 80%); }
  .headline { position: absolute; left: 0; width: 199px; top: 347px; text-align: center; color: var(--white); }
  .headline span { display: block; }
  .headline .h-1 { font-size: 23px; }
  .headline .h-2 { font-size: 34px; margin-top: -1px; }
  .headline .h-3 { font-size: 23px; margin-top: -1px; }
  .headline .h-4 { font-size: 14.5px; margin-top: 1px; }

  /* Services */
  .services-title { top: 10px; color: var(--white); }
  .services-divider { top: 37px; }
  .service { position: absolute; left: 0; right: 0; text-align: center; }
  .service-thumb { width: 80px; height: 80px; margin: 0 auto; clip-path: polygon(29% 0,71% 0,100% 29%,100% 71%,71% 100%,29% 100%,0 71%,0 29%); background: var(--white); padding: 1.5px; }
  .service-thumb i { display: block; width: 100%; height: 100%; clip-path: inherit; }
  .service-name { font-size: 11.2px; font-weight: 500; margin-top: 15px; line-height: 14px; white-space: nowrap; letter-spacing: -0.1px; }
  .service-desc { font-size: 7.7px; font-weight: 300; margin-top: 3px; white-space: nowrap; }
  .panel--services .service { color: var(--white); }
  .panel--supply .service { color: var(--white); }
  .panel--supply .service-desc { color: var(--pale); }

  /* Network */
  .partners-title { top: 22px; color: var(--navy); }
  .partners-divider { top: 49px; background: var(--blue); }
  .partners-divider::after { background: var(--blue); }
  .partner { position: absolute; left: 0; right: 0; text-align: center; font-size: 16px; font-weight: 500; color: #6b6f75; letter-spacing: 1px; }
  .deco { position: absolute; left: 0; top: 0; width: 224px; height: 450px; }
  .clients-title { top: 264px; color: var(--navy); }
  .clients-divider { top: 292px; background: var(--blue); }
  .clients-divider::after { background: var(--blue); }
  .client-grid { position: absolute; left: 10px; top: 322px; width: 206px; display: grid; grid-template-columns: repeat(4, 1fr); row-gap: 17px; column-gap: 4px; }
  .client { font-size: 6.4px; font-weight: 600; color: var(--navy); text-align: center; line-height: 17px; white-space: nowrap; overflow: hidden; }
</style>
</head>
<body>

<section class="sheet sheet--outside">
  <div class="panel panel--about">
    <h2 class="about-title display">About <span class="accent">Us</span></h2>
    <div class="about-divider"></div>
    <h3 class="about-subtitle">The Journey of Environmental Service Excellence</h3>
    <p class="about-body">Originating from a desire to provide more robust technical support to the Australia wide industrial sector, we began our journey by focusing on the critical need for reliable dust management. We recognised that many facilities struggled with maintaining complex filtration systems, and we stepped in to offer a more dedicated, hands-on approach. This foundation allowed us to build a reputation based on technical merit and unwavering support for our clients.</p>
    <div class="about-photo" role="img" aria-label="Photo of a dust collector tube sheet with filter bag holes"></div>
    <div class="badge display"><span class="badge-years">25 Year</span><span class="badge-label">Experience</span></div>
  </div>

  <div class="panel panel--contact">
    <h2 class="section-title contact-title display">Contact Us</h2>
    <div class="divider contact-divider"></div>
    <div class="contact-icon" style="top:93px">
      <svg viewBox="0 0 24 24" fill="none" stroke="#fff" stroke-width="2.4" stroke-linecap="round" stroke-linejoin="round"><path d="M22 16.9v3a2 2 0 0 1-2.2 2 19.8 19.8 0 0 1-8.6-3.1 19.5 19.5 0 0 1-6-6A19.8 19.8 0 0 1 2.1 4.2 2 2 0 0 1 4.1 2h3a2 2 0 0 1 2 1.7c.1.9.4 1.800.7 2.7a2 2 0 0 1-.5 2.1L8 9.8a16 16 0 0 0 6 6l1.3-1.3a2 2 0 0 1 2.1-.4c.9.3 1.8.6 2.7.7a2 2 0 0 1 1.7 2z"/></svg>
    </div>
    <div class="contact-phone display">0400 512 738</div>
    <div class="contact-icon" style="top:164px">
      <svg viewBox="0 0 24 24" fill="none" stroke="#fff" stroke-width="2.2" stroke-linejoin="round"><rect x="2" y="5" width="20" height="14" rx="1.5"/><path d="M2 6l10 7 10-7"/></svg>
    </div>
    <div class="contact-email">hello@plmorvex.au</div>
    <div class="contact-social"></div>
    <div class="contact-social-name">Netlink</div>
    <div class="contact-bars"></div>
    <div class="contact-strip"></div>
    <div class="contact-photo" role="img" aria-label="Photo of rows of filter cages inside a baghouse"></div>
  </div>

  <div class="panel panel--cover">
    <div class="cover-photo" role="img" aria-label="Photo of a technician in a hard hat inspecting rolled filter bags in an industrial plant"></div>
    <div class="brand-box"></div>
    <div class="brand"><span class="brand-dot"></span><span class="brand-name">PLMORVEX</span></div>
    <div class="brand-tag">ENVIRONMENTAL<br>SERVICES</div>
    <div class="cover-corner"></div>
    <div class="cover-panel"></div>
    <div class="cover-bars"></div>
    <h1 class="headline display">
      <span class="h-1">Premium Dust</span>
      <span class="h-2">Collector</span>
      <span class="h-3">Supply &amp; Expert</span>
      <span class="h-4">Maintenance Solutions</span>
    </h1>
  </div>
</section>

<section class="sheet sheet--inside">
  <div class="panel panel--services">
    <h2 class="section-title services-title display">Our Services</h2>
    <div class="divider services-divider"></div>
    <div class="service" style="top:51px">
      <div class="service-thumb"><i role="img" aria-label="Photo of a dust collector tube sheet" style="background:linear-gradient(150deg,#9aa3ab,#4d555c)"></i></div>
      <div class="service-name">Dust Collectors Servicing</div>
      <div class="service-desc">Industrial maintenance, dust collector repair</div>
    </div>
    <div class="service" style="top:187px">
      <div class="service-thumb"><i role="img" aria-label="Photo of filter cages fitted in a perforated plate" style="background:linear-gradient(150deg,#c4cacf,#5b6268)"></i></div>
      <div class="service-name">Dust Collectors Regular Maintenance</div>
      <div class="service-desc">Scheduled servicing, system upkeep</div>
    </div>
    <div class="service" style="top:321px">
      <div class="service-thumb"><i role="img" aria-label="Photo of a worker installing filtration bags" style="background:linear-gradient(150deg,#6b6f9a,#b7b0c8 50%,#d9d23a)"></i></div>
      <div class="service-name">Filtration Bags Install</div>
      <div class="service-desc">Baghouse installation, filter fitting</div>
    </div>
  </div>

  <div class="panel panel--supply">
    <div class="service" style="top:31px">
      <div class="service-thumb"><i role="img" aria-label="Photo of industrial filter bags" style="background:linear-gradient(150deg,#e9e6df,#a47a52 45%,#e6dcc6)"></i></div>
      <div class="service-name">Filtration Bags Supply</div>
      <div class="service-desc">Industrial filter bags, dust media</div>
    </div>
    <div class="service" style="top:167px">
      <div class="service-thumb"><i role="img" aria-label="Photo of dust collector controller units" style="background:linear-gradient(150deg,#ffffff,#9aa1a6 50%,#f4f4f4)"></i></div>
      <div class="service-name">Dust Collectors Spare Parts Supply</div>
      <div class="service-desc">Replacement filters, collector components</div>
    </div>
    <div class="service" style="top:301px">
      <div class="service-thumb"><i role="img" aria-label="Photo of an industrial dust collector system" style="background:linear-gradient(150deg,#8a8c86,#cfd0cc 50%,#6f726c)"></i></div>
      <div class="service-name">Dust Collectors Supply</div>
      <div class="service-desc">Filtration system units, industrial supply</div>
    </div>
  </div>

  <div class="panel panel--network">
    <svg class="deco" viewBox="0 0 224 450" aria-hidden="true">
      <polygon points="83,198 224,146 224,172 124,210" fill="var(--sky)"/>
      <polygon points="0,171 124,210 0,254" fill="var(--navy)"/>
    </svg>
    <h2 class="section-title partners-title display">Our <span class="accent">Partners</span></h2>
    <div class="divider partners-divider"></div>
    <div class="partner" style="top:80px">Kestral Filtra</div>
    <div class="partner" style="top:121px;color:var(--ink)">VARONDE</div>
    <h2 class="section-title clients-title display">Our <span class="accent">Clients</span></h2>
    <div class="divider clients-divider"></div>
    <div class="client-grid">
      <span class="client">Harlow Brick</span>
      <span class="client">Quayside</span>
      <span class="client">Orrin Cement</span>
      <span class="client">Calder</span>
      <span class="client">Brayfield</span>
      <span class="client">Veltrom</span>
      <span class="client">Ductel</span>
      <span class="client">Civora</span>
      <span class="client">Goldrow</span>
      <span class="client">KMT</span>
      <span class="client">Belstow</span>
      <span class="client">RDX</span>
    </div>
  </div>
</section>

</body>
</html>
```